Willow Crest Website

We need a website that has clean, asian looking images that relax and motivate people to come into our integrated medical center. My current website is www.pinebrookcare.example and I would like the design for Willow Crest Health Solutions to be similar but more inviting with video content and a product purchase store as well. A moving banner would be nice too. When people are looking for ways of losing weight or getting out of pain we want them to make the connection that we have the solution. This website needs to provide sufficient information so that patients are well informed and choose us as their health provider before they ever walk through our doors. We offer comprehensive natural medicine that is based on the principles that the body can heal itself when given the right conditions. Our services include medical weight loss and hormone balancing, acupuncture and chinese herbal medicine, physical medicine, trigger point injections, allergy testing and joint rehabilitation. The Medical Doctor and Licensed Acupuncturist work as a team to provide optimal care that is catered to each individual who comes through our doors.
Updates

Target Market(s)

40 to 50 year olds who want to lose weight or have pain issues.

Industry/Entity Type

Medical

Requirements
Must have
• Use photos from our website www.pinebrookcare.example or similar content. Video content. Moving banner with relaxing images.
Nice to have
• Happy, healthy looking people. Medical Doctors working as a team. Friendly staff in a cutting edge facility.
Should not have
• Papyrus font, or big bold words.

```html
<!DOCTYPE html>
<html lang="en">
<head>
<meta charset="utf-8">
<title>Willow Crest Health Solutions – E-Shop</title>
<link href="https://fonts.googleapis.com/css2?family=Maven+Pro:wght@400;500;700&display=swap" rel="stylesheet">
<style>
:root{
  --wood:#ece5d7;
  --wood-line:#e2d9c8;
  --band-top:#e3d2b4;
  --band-bottom:#d9c7a6;
  --olive:#a29e7c;
  --text:#6e5e52;
  --text-soft:#8a7b6f;
  --nav:#a39586;
  --panel:#ded3c1;
  --panel-line:#cdbfa9;
  --footer:#857369;
  --footer-text:#eee3d6;
  --contact:#c5bd9f;
  --contact-text:#5d5347;
  --icon:#c7baa8;
  --ribbon:#bfb693;
  --white:#ffffff;
  --frame:#8a6e5a;
}
*{box-sizing:border-box;margin:0;padding:0}
html,body{width:1000px;height:1200px;overflow:hidden}
body{
  position:relative;
  font-family:"Maven Pro",sans-serif;
  color:var(--text);
  background:var(--wood) repeating-linear-gradient(180deg,transparent 0 38px,var(--wood-line) 38px 40px);
}
.abs{position:absolute}

/* top navigation */
.main-nav{left:461px;top:46px;display:flex;gap:25px;font-size:9px;font-weight:700;letter-spacing:1.2px;text-transform:uppercase}
.main-nav a{color:var(--nav);text-decoration:none;position:relative}
.main-nav a.current{color:var(--text);border-bottom:1px solid var(--text);padding-bottom:2px}
.main-nav a.current::after{content:"";position:absolute;left:50%;top:22px;margin-left:-6px;border:6px solid transparent;border-top-color:var(--wood)}

.title-band{left:0;top:75px;width:1000px;height:75px;background:linear-gradient(180deg,var(--band-top),var(--band-bottom));box-shadow:0 2px 3px rgba(0,0,0,.12) inset}
.page-title{left:333px;top:94px;font-size:30px;font-weight:400;color:var(--text-soft)}

/* brand block */
.brand{left:131px;top:56px;width:175px;height:235px;background:var(--olive);box-shadow:0 2px 4px rgba(0,0,0,.15);text-align:center;color:var(--white)}
.brand::before{content:"";position:absolute;left:-8px;top:0;border-style:solid;border-width:0 8px 10px 0;border-color:transparent #7c7858 transparent transparent}
.brand-art{position:absolute;left:19px;top:18px;width:138px;height:150px;background:linear-gradient(180deg,#d0cab1,#b3ad8e)}
.brand-name{position:absolute;left:0;right:0;top:176px;font-size:24px;line-height:28px;font-weight:700;white-space:nowrap}
.brand-tag{position:absolute;left:0;right:0;top:208px;font-size:12px;line-height:14px;letter-spacing:.6px;white-space:nowrap}

/* intro copy */
.intro{left:331px;top:174px;width:545px;font-size:11px;line-height:19px;color:var(--text)}
.intro p+p{margin-top:19px}

/* category menu */
.category-menu{left:131px;top:319px;width:175px;list-style:none;font-size:13px}
.category-menu li{height:38px;line-height:37px;padding-left:7px;border-bottom:2px solid var(--panel-line)}
.category-menu li.active{background:var(--panel);font-weight:700;border-top:2px solid var(--panel-line)}

/* order summary */
.order-box{left:131px;top:506px;width:175px;height:178px;background:var(--panel);border:1px solid var(--panel-line);padding:18px 13px;font-size:12.5px}
.order-box h3{font-size:12px;font-weight:700}
.order-count{margin-top:22px;padding-bottom:9px;border-bottom:1px dotted var(--text-soft)}
.order-total{margin-top:10px;display:flex;justify-content:space-between}
.proceed{position:absolute;right:14px;top:136px;width:71px;height:25px;border:1px solid #b8a996;border-radius:6px;background:linear-gradient(#fff,#eee8df);font:700 12px "Maven Pro",sans-serif;color:var(--text);box-shadow:0 1px 2px rgba(0,0,0,.2)}

/* product grid */
.product{width:160px;height:185px}
.product-frame{position:absolute;left:0;top:0;width:160px;height:131px;background:#e2d7c4;overflow:hidden}
.product-photo{position:absolute;left:12px;top:12px;width:135px;height:107px;border:2px solid var(--frame);background:var(--white);box-shadow:0 2px 4px rgba(0,0,0,.25)}
.product-photo span{position:absolute;inset:8px;border-radius:4px}
.promo{position:absolute;right:0;top:0}
.product-name{position:absolute;left:0;top:140px;font-size:14px;font-weight:500}
.product-price{position:absolute;left:0;top:156px;font-size:10.5px}
.product-actions{position:absolute;right:2px;top:137px;display:flex;gap:6px}
.icon-btn{width:19px;height:19px;border-radius:50%;background:var(--icon);display:flex;align-items:center;justify-content:center;color:var(--white);font-size:11px;font-weight:700}

.pager{left:752px;top:853px;display:flex;align-items:center;gap:8px;font-size:12px}
.pager-btn{width:18px;height:18px;border-radius:50%;background:var(--icon);display:flex;align-items:center;justify-content:center}

/* footer */
.site-footer{left:0;top:937px;width:1000px;height:224px;background:var(--footer)}
.footer-col{top:965px;width:113px;font-size:9px;color:var(--footer-text);list-style:none}
.footer-col li{line-height:19px}
.footer-col .head{font-weight:700;letter-spacing:.6px;text-transform:uppercase}
.footer-col .sep{height:10px;border-bottom:1px dotted var(--footer-text);margin-bottom:10px;opacity:.7}
.calligraphy{left:544px;top:955px;width:40px;height:180px;background:linear-gradient(180deg,rgba(110,95,86,.55),rgba(110,95,86,.3));border-radius:3px}
.contact-card{left:631px;top:919px;width:238px;height:150px;background:var(--contact);padding:13px 13px;color:var(--contact-text);box-shadow:0 3px 5px rgba(0,0,0,.25)}
.contact-card::before{content:"";position:absolute;left:-12px;top:0;border-style:solid;border-width:0 12px 14px 0;border-color:transparent #a49c80 transparent transparent}
.contact-card h2{font-size:18px;font-weight:700}
.contact-card p{font-size:10.5px;line-height:19px;margin-top:2px}
.contact-line{display:flex;align-items:center;gap:7px;font-size:12.5px;font-weight:700;margin-top:10px}
.social{left:714px;top:1091px;display:flex;gap:14px}
.social span{width:28px;height:28px;border-radius:50%;background:#5e4f47}
.copyright{left:132px;top:1174px;font-size:10px;color:var(--text)}
</style>
</head>
<body>

<nav class="main-nav abs">
  <a href="#">Home</a><a href="#">About us</a><a href="#">Acupuncture</a><a href="#">Healthcare</a><a href="#" class="current">Shop</a><a href="#">Contact</a>
</nav>

<div class="title-band abs"></div>
<h1 class="page-title abs">E-Shop</h1>

<div class="brand abs">
  <div class="brand-art" role="img" aria-label="Silhouette artwork of a windswept tree on a rock"></div>
  <div class="brand-name">Willow Crest</div>
  <div class="brand-tag">HEALTH SOLUTIONS</div>
</div>

<div class="intro abs">
  <p>Molestias exceptur sint dupic non provident, simil tempor sunt in culpa qui deserunt mollit anim id est labo-rum et dolor fup. Et harumd dereund facilis est er expedit distinct.</p>
  <p>Nam liber tempor cum nobis eligend optio comgue n</p>
</div>

<ul class="category-menu abs">
  <li class="active">Massage Oils</li>
  <li>Herbal products</li>
  <li>Nutrition</li>
  <li>Natural therapeutics</li>
</ul>

<div class="order-box abs">
  <h3>Your order :</h3>
  <div class="order-count">6 products</div>
  <div class="order-total"><span>Total :</span><span>198 $</span></div>
  <button class="proceed">Proceed</button>
</div>

<div class="product abs" style="left:331px;top:281px">
  <div class="product-frame"><div class="product-photo"><span role="img" aria-label="Open jar of olive balm with an olive branch" style="background:linear-gradient(135deg,#eef0d4,#c9c97a)"></span></div></div>
  <div class="product-name">OliveOil</div><div class="product-price">24 $ -250 ml</div>
  <div class="product-actions"><span class="icon-btn">i</span><span class="icon-btn"><svg width="11" height="9" viewBox="0 0 11 9"><path d="M0 2h11L9 8H2z" fill="#fff"/></svg></span></div>
</div>
<div class="product abs" style="left:520px;top:281px">
  <div class="product-frame"><div class="product-photo"><span role="img" aria-label="Amber gel capsules spilling from a jar" style="background:linear-gradient(135deg,#fbe3a6,#e9a229)"></span></div></div>
  <div class="product-name">OliveOil</div><div class="product-price">24 $ -250 ml</div>
  <div class="product-actions"><span class="icon-btn">i</span><span class="icon-btn"><svg width="11" height="9" viewBox="0 0 11 9"><path d="M0 2h11L9 8H2z" fill="#fff"/></svg></span></div>
</div>
<div class="product abs" style="left:709px;top:281px">
  <div class="product-frame"><div class="product-photo"><span role="img" aria-label="Fresh mint leaves on white cream" style="background:linear-gradient(135deg,#f4f6f0,#6aa33d)"></span></div>
    <svg class="promo" width="70" height="70" viewBox="0 0 70 70"><path d="M18 0h24l28 28v24z" fill="#bfb693"/><text x="0" y="0" transform="translate(51 20) rotate(45)" text-anchor="middle" dominant-baseline="central" font-family="Maven Pro,sans-serif" font-size="10" font-weight="700" letter-spacing=".5" fill="#fff">PROMO</text></svg></div>
  <div class="product-name">OliveOil</div><div class="product-price">24 $ -250 ml</div>
  <div class="product-actions"><span class="icon-btn">i</span><span class="icon-btn"><svg width="11" height="9" viewBox="0 0 11 9"><path d="M0 2h11L9 8H2z" fill="#fff"/></svg></span></div>
</div>

<div class="product abs" style="left:331px;top:469px">
  <div class="product-frame"><div class="product-photo"><span role="img" aria-label="Cream jar with red rose petals" style="background:linear-gradient(135deg,#f4eeec,#d94a3a)"></span></div>
    <svg class="promo" width="70" height="70" viewBox="0 0 70 70"><path d="M18 0h24l28 28v24z" fill="#bfb693"/><text x="0" y="0" transform="translate(51 20) rotate(45)" text-anchor="middle" dominant-baseline="central" font-family="Maven Pro,sans-serif" font-size="10" font-weight="700" letter-spacing=".5" fill="#fff">PROMO</text></svg></div>
  <div class="product-name">OliveOil</div><div class="product-price">24 $ -250 ml</div>
  <div class="product-actions"><span class="icon-btn">i</span><span class="icon-btn"><svg width="11" height="9" viewBox="0 0 11 9"><path d="M0 2h11L9 8H2z" fill="#fff"/></svg></span></div>
</div>
<div class="product abs" style="left:520px;top:469px">
  <div class="product-frame"><div class="product-photo"><span role="img" aria-label="Spa soaps, lavender and lotion bottles" style="background:linear-gradient(135deg,#f5f1ea,#a0734d)"></span></div></div>
  <div class="product-name">OliveOil</div><div class="product-price">24 $ -250 ml</div>
  <div class="product-actions"><span class="icon-btn">i</span><span class="icon-btn"><svg width="11" height="9" viewBox="0 0 11 9"><path d="M0 2h11L9 8H2z" fill="#fff"/></svg></span></div>
</div>
<div class="product abs" style="left:709px;top:469px">
  <div class="product-frame"><div class="product-photo"><span role="img" aria-label="Rosemary sprigs with amber dropper bottles" style="background:linear-gradient(135deg,#eef1e8,#7a4a1e)"></span></div></div>
  <div class="product-name">OliveOil</div><div class="product-price">24 $ -250 ml</div>
  <div class="product-actions"><span class="icon-btn">i</span><span class="icon-btn"><svg width="11" height="9" viewBox="0 0 11 9"><path d="M0 2h11L9 8H2z" fill="#fff"/></svg></span></div>
</div>

<div class="product abs" style="left:331px;top:657px">
  <div class="product-frame"><div class="product-photo"><span role="img" aria-label="Green herbal cosmetic jars and pump bottle" style="background:linear-gradient(135deg,#f4f6ea,#a9bf5a)"></span></div></div>
  <div class="product-name">OliveOil</div><div class="product-price">24 $ -250 ml</div>
  <div class="product-actions"><span class="icon-btn">i</span><span class="icon-btn"><svg width="11" height="9" viewBox="0 0 11 9"><path d="M0 2h11L9 8H2z" fill="#fff"/></svg></span></div>
</div>
<div class="product abs" style="left:520px;top:657px">
  <div class="product-frame"><div class="product-photo"><span role="img" aria-label="Purple glass bottles with wildflowers" style="background:linear-gradient(135deg,#f3f1f6,#5d3c9c)"></span></div></div>
  <div class="product-name">OliveOil</div><div class="product-price">24 $ -250 ml</div>
  <div class="product-actions"><span class="icon-btn">i</span><span class="icon-btn"><svg width="11" height="9" viewBox="0 0 11 9"><path d="M0 2h11L9 8H2z" fill="#fff"/></svg></span></div>
</div>
<div class="product abs" style="left:709px;top:657px">
  <div class="product-frame"><div class="product-photo"><span role="img" aria-label="Brown eco-friendly hanging tags" style="background:linear-gradient(135deg,#f6efe8,#9a5a30)"></span></div></div>
  <div class="product-name">OliveOil</div><div class="product-price">24 $ -250 ml</div>
  <div class="product-actions"><span class="icon-btn">i</span><span class="icon-btn"><svg width="11" height="9" viewBox="0 0 11 9"><path d="M0 2h11L9 8H2z" fill="#fff"/></svg></span></div>
</div>

<div class="pager abs">
  <span class="pager-btn"><svg width="8" height="8" viewBox="0 0 8 8"><path d="M6 0v8L1 4z" fill="#6e5e52"/></svg></span>
  <span>Page 1 of 3</span>
  <span class="pager-btn"><svg width="8" height="8" viewBox="0 0 8 8"><path d="M2 0v8l5-4z" fill="#6e5e52"/></svg></span>
</div>

<footer class="site-footer abs"></footer>

<ul class="footer-col abs" style="left:131px">
  <li class="head">• Home</li><li class="sep"></li>
  <li class="head">• About us</li><li>• Philosophy</li><li>• Our team</li>
</ul>
<ul class="footer-col abs" style="left:257px">
  <li class="head">• Acupuncture</li><li>• Information</li><li>• History</li><li>• Seitai Shinpo</li><li class="sep"></li>
  <li class="head">• Healthcare</li><li>• Programme</li><li>• So Tai Ho</li><li>• Therapy</li>
</ul>
<ul class="footer-col abs" style="left:381px">
  <li class="head">• Shop</li><li>• Massage Oil</li><li>• Therapeutics</li><li>• Herbal</li><li>• Beauty products</li><li class="sep"></li>
  <li class="head">• Contact</li>
</ul>

<div class="calligraphy abs" role="img" aria-label="Faint vertical brush calligraphy meaning health and happiness"></div>

<div class="contact-card abs">
  <h2>Contact us</h2>
  <p>Lorem ipsum do pland sit amet, con sectetur a dip sching.</p>
  <div class="contact-line"><svg width="13" height="22" viewBox="0 0 13 22"><rect x="1" y="1" width="11" height="20" rx="2" fill="none" stroke="#5d5347" stroke-width="2"/><rect x="3" y="4" width="7" height="7" fill="#5d5347"/><rect x="3" y="13" width="7" height="5" fill="#5d5347"/></svg>(555) 014-2290</div>
  <div class="contact-line"><svg width="15" height="12" viewBox="0 0 15 12"><rect width="15" height="12" rx="1" fill="#5d5347"/><path d="M1 1l6.5 5L14 1" fill="none" stroke="#c5bd9f" stroke-width="1.3"/></svg>info@willowcrest.example</div>
</div>

<div class="social abs"><span></span><span></span><span></span><span></span></div>

<div class="copyright abs">© Copyright Willow Crest Healthcare 2012 - Privacy policy</div>

</body>
</html>
```